Copper lark buildworks

Copper lark buildworks is a small construction company.
Who is a licenced builder, Carpenter, joiner,
working on heritage ,new build, speacial projects and sometimes furniture

Industry/Entity Type

Construction

```html
<!DOCTYPE html>
<html lang="en">
<head>
<meta charset="utf-8">
<title>Copper lark buildworks — business cards</title>
<link rel="stylesheet" href="https://fonts.googleapis.com/css2?family=Open+Sans:wght@400;600;700&display=swap">
<style>
  :root {
    --backdrop: #d9dadb;
    --card-black: #050505;
    --card-charcoal: #141414;
    --band-grey: #101010;
    --disc-grey: #171717;
    --green-bright: #19e63a;
    --green-mid: #10b82c;
    --green-deep: #1e6d14;
    --shadow: rgba(0, 0, 0, 0.35);
  }

  * { box-sizing: border-box; margin: 0; padding: 0; }

  html, body {
    width: 1200px;
    height: 900px;
    overflow: hidden;
  }

  body {
    background: var(--backdrop);
    font-family: "Open Sans", sans-serif;
    position: relative;
  }

  .business-card {
    position: absolute;
    width: 460px;
    height: 270px;
    overflow: hidden;
    box-shadow: 0 10px 24px var(--shadow);
  }

  /* Front of the card */
  .card-front {
    left: 150px;
    top: 170px;
    background: linear-gradient(160deg, var(--card-black) 0%, var(--card-charcoal) 100%);
    display: flex;
    align-items: center;
    justify-content: center;
  }

  .front-wordmark {
    display: flex;
    align-items: center;
    gap: 12px;
  }

  .brand-square {
    width: 22px;
    height: 22px;
    background: var(--green-bright);
  }

  .brand-name {
    color: var(--green-bright);
    font-weight: 700;
    font-size: 22px;
    letter-spacing: 0.02em;
    text-transform: uppercase;
  }

  /* Back of the card */
  .card-back {
    left: 600px;
    top: 470px;
    background: var(--card-black);
  }

  .name-band {
    position: absolute;
    left: 0;
    top: 72px;
    width: 100%;
    height: 72px;
    background: var(--band-grey);
  }

  .logo-disc {
    position: absolute;
    left: 250px;
    top: -40px;
    width: 300px;
    height: 300px;
    border-radius: 50%;
    background: var(--disc-grey);
  }

  .accent-bar {
    position: absolute;
    left: 250px;
    top: 170px;
    width: 210px;
    height: 24px;
    display: flex;
  }
  .accent-bar span { flex: 1; }
  .accent-bar .seg-bright { background: var(--green-bright); }
  .accent-bar .seg-mid { background: var(--green-mid); }
  .accent-bar .seg-deep { background: var(--green-deep); }

  .person {
    position: absolute;
    left: 32px;
    top: 92px;
    color: var(--green-bright);
    line-height: 1.15;
  }
  .person-name {
    font-size: 17px;
    font-variant: small-caps;
    font-weight: 400;
  }
  .person-role {
    font-size: 12px;
    color: var(--green-mid);
  }

  .back-company {
    position: absolute;
    left: 140px;
    top: 205px;
    color: var(--green-bright);
    font-weight: 700;
    font-size: 13px;
    text-transform: uppercase;
    letter-spacing: 0.02em;
  }

  .contact-line {
    position: absolute;
    left: 160px;
    top: 232px;
    display: flex;
    align-items: center;
    gap: 8px;
    color: var(--green-mid);
    font-size: 11px;
  }
  .phone-icon { width: 14px; height: 14px; }
</style>
</head>
<body>

  <section class="business-card card-front" aria-label="Card front">
    <div class="front-wordmark">
      <div class="brand-square"></div>
      <p class="brand-name">Copper lark buildworks</p>
    </div>
  </section>

  <section class="business-card card-back" aria-label="Card back">
    <div class="name-band"></div>
    <div class="logo-disc"></div>
    <div class="accent-bar">
      <span class="seg-bright"></span>
      <span class="seg-mid"></span>
      <span class="seg-deep"></span>
    </div>

    <div class="person">
      <p class="person-name">Milo Hartley</p>
      <p class="person-role">general manager</p>
    </div>

    <p class="back-company">Copper lark buildworks</p>

    <div class="contact-line">
      <svg class="phone-icon" viewBox="0 0 24 24" aria-hidden="true">
        <circle cx="12" cy="12" r="12" fill="#10b82c"/>
        <path d="M8.2 6.5l1.8-.4 1.1 2.7-1.2.9c.6 1.4 1.7 2.5 3.1 3.1l.9-1.2 2.7 1.1-.4 1.8c-.1.5-.6.8-1.1.8-4.1-.3-7.4-3.6-7.7-7.7 0-.5.3-1 .8-1.1z" fill="#050505"/>
      </svg>
      <span>041 372 0964</span>
    </div>
  </section>

</body>
</html>
```